Business Management Fortress

Assist with enhancing a powerpoint slide by providing a few design options for consideration. I have a template but open to any creative ideas.

Target Market(s)

Internal employees and stakeholders

Industry/Entity Type

Business Management, Finance, Accounting

Requirements
Must have
• Maintain a fortress, temple, or pyramid schema
Nice to have
• Scenic Background

```html
<!DOCTYPE html>
<html lang="en">
<head>
<meta charset="utf-8">
<title>Business Management Fortress</title>
<link href="https://fonts.googleapis.com/css2?family=Carlito:wght@400;700&display=swap" rel="stylesheet">
<style>
  :root {
    --sky-top: #bac8e2;
    --sky-mid: #8fa6d0;
    --ridge-deep: #2b55a0;
    --ink: #0d0d0f;
    --rule: #3a3f4a;
    --veil: rgba(255,255,255,0.48);
    --sun: rgba(255,255,255,0.28);
  }
  html, body { margin: 0; padding: 0; overflow: hidden; }
  body { width: 1200px; height: 675px; }
  .slide {
    position: relative; width: 1200px; height: 675px; overflow: hidden;
    font-family: "Carlito", "Calibri", sans-serif; color: var(--ink);
  }
  .scenery {
    position: absolute; inset: 0;
    background:
      linear-gradient(200deg, transparent 45%, rgba(43,85,160,0.55) 75%, var(--ridge-deep) 100%),
      linear-gradient(180deg, var(--sky-top) 0%, var(--sky-mid) 45%, #6483c0 75%, #4a6cb0 100%);
  }
  .pyramid { position: absolute; inset: 0; }
  .title {
    position: absolute; left: 69px; top: 60px; margin: 0;
    font-size: 39px; font-weight: 700; line-height: 53px;
  }
  .label {
    position: absolute; font-weight: 700; font-size: 28px; line-height: 36px; white-space: nowrap;
  }
  .label.center { transform: translateX(-50%); text-align: center; }
  .label.right { transform: translateX(-100%); text-align: right; }
  .duties {
    position: absolute; left: 517px; top: 554px; margin: 0;
    font-size: 29px; line-height: 36px; font-weight: 400; white-space: nowrap;
  }
</style>
</head>
<body>
<div class="slide">
  <div class="scenery" role="img" aria-label="Misty blue mountain ranges with a figure standing on a peak, arms raised"></div>

  <svg class="pyramid" width="1200" height="675" viewBox="0 0 1200 675" aria-hidden="true">
    <polygon points="895,74 1200,296 1200,675 75,675" fill="var(--veil)"/>
    <circle cx="897" cy="109" r="71" fill="var(--sun)"/>
    <g stroke="var(--rule)" stroke-width="0.8">
      <line x1="800" y1="206" x2="800" y2="332"/>
      <line x1="946" y1="206" x2="946" y2="332"/>
      <line x1="599" y1="348" x2="1161" y2="348"/>
      <line x1="621" y1="366" x2="621" y2="491"/>
      <line x1="781" y1="366" x2="781" y2="491"/>
      <line x1="994" y1="366" x2="994" y2="491"/>
      <line x1="371" y1="509" x2="1161" y2="509"/>
      <line x1="484" y1="526" x2="484" y2="651"/>
    </g>
    <polygon points="485,567 497,589 485,611" fill="var(--ink)"/>
  </svg>

  <h1 class="title">Business Management<br>Fortress</h1>

  <div class="label" style="left:691px; top:253px;">Leader</div>
  <div class="label" style="left:827px; top:253px;">Partner</div>
  <div class="label" style="left:973px; top:253px;">Profitability</div>

  <div class="label" style="left:504px; top:411px;">People</div>
  <div class="label" style="left:634px; top:411px;">Innovation</div>
  <div class="label center" style="left:887px; top:394px;">Business<br>Intelligence</div>
  <div class="label right" style="left:1156px; top:394px;">Strategic<br>Alliances</div>

  <div class="label" style="left:268px; top:554px;">Fiduciary<br>Responsibilities</div>
  <p class="duties">Accurate Financials / Internal Controls / Brand<br>Protection / Compliance / Ethics / Cost Management</p>
</div>
</body>
</html>
```